IT Security Company Website

We would like to create a new look for our current company site velmora.io. The company offercyber security services for banks, goverment etc. Therefore a very professional look is important. We need at least 2 pages designed.

Target Market(s)

B2B

Coding

Coded - Design and coding required

Number of Pages Required

1 page

```html
<!DOCTYPE html>
<html lang="en">
<head>
<meta charset="utf-8">
<title>Velmora – Defend Against Cyber-Attacks</title>
<link rel="stylesheet" href="https://fonts.googleapis.com/css2?family=Roboto:wght@300;400;500;700&display=swap">
<style>
:root{
  --gold:#f0c239;
  --gold-deep:#d9a92a;
  --gold-soft:#ead28a;
  --ink:#1b1b1f;
  --text:#5d5d66;
  --muted:#8a8a92;
  --navy:#1b1746;
  --violet:#4a2f8f;
  --paper:#f4f4f6;
  --slate:#66666e;
  --brown:#5a4010;
  --white:#ffffff;
}
*{box-sizing:border-box;margin:0;padding:0}
html,body{width:1200px;height:4478px;overflow:hidden}
body{position:relative;background:var(--white);font-family:'Roboto',sans-serif;color:var(--ink)}
.abs{position:absolute}
a{color:inherit;text-decoration:none}

/* hero */
.hero-bg{position:absolute;left:0;top:0;width:1200px;height:1002px;background:var(--paper)}
.hero-shape{position:absolute;left:0;top:0}
.brand{position:absolute;font-family:'Roboto',sans-serif;font-weight:300;letter-spacing:1px}
.brand-hero{left:113px;top:36px;font-size:38px;color:var(--white)}
.nav{position:absolute;left:434px;top:44px;display:flex;gap:30px;font-size:17px;color:#e8e6f4}
.nav .active{color:var(--white);border-bottom:2px solid var(--white);padding-bottom:5px}
.contact-btn{position:absolute;left:917px;top:31px;width:166px;height:46px;border-radius:4px;background:#f3f3f6;color:#3a3a42;font-size:16px;display:flex;align-items:center;justify-content:center;gap:10px}
.hero-title{position:absolute;left:0;width:1200px;text-align:center;font-weight:500;color:var(--white)}
.h1a{top:222px;font-size:42px}
.h1b{top:275px;font-size:66px;color:var(--gold);letter-spacing:1px}
.h1c{top:352px;font-size:42px}
.hero-lead{position:absolute;left:250px;top:412px;width:700px;text-align:center;font-size:15.5px;line-height:26px;color:#e6e3f2}
.demo-btn{position:absolute;left:496px;top:492px;width:208px;height:50px;border-radius:25px;background:var(--gold);color:var(--ink);font-size:15px;font-weight:500;display:flex;align-items:center;justify-content:center}

.partners{position:absolute;top:858px;left:0;width:1200px;display:flex;justify-content:center;gap:70px}
.partner{height:56px;background:#cfcfd4;border-radius:6px}

/* about */
.about{position:absolute;top:1002px;left:0;width:1200px;height:542px;background:var(--white)}
.shield{position:absolute;border-radius:0 0 50% 50% / 0 0 52% 52%;border-bottom:7px solid var(--gold);border-left:3px solid var(--gold-deep);border-right:3px solid var(--gold-deep)}
.shield-about{left:150px;top:83px;width:372px;height:392px;background:linear-gradient(160deg,#0e3d6b 0%,#1f7d8f 45%,#7b5a1c 100%)}
.section-title{font-weight:500;font-size:40px;color:var(--ink)}
.section-title .hl{color:var(--gold)}
.about-title{position:absolute;left:600px;top:108px}
.body-copy{font-size:14.3px;line-height:25px;color:var(--text)}
.about-copy{position:absolute;left:600px;top:170px;width:470px}
.about-copy p+p{margin-top:14px}
.outline-btn{position:absolute;width:136px;height:38px;border:2px solid var(--gold-soft);border-radius:19px;color:var(--gold);font-size:12px;display:flex;align-items:center;justify-content:center}
.dot-line-h{position:absolute;height:0;border-top:2px dotted var(--gold)}
.dot-end{position:absolute;width:7px;height:7px;border-radius:50%;background:var(--gold)}

/* risks */
.risks{position:absolute;top:1544px;left:0;width:1200px;height:661px;background:linear-gradient(180deg,#ecd48a 0%,#e3c36a 60%,#d8b24b 100%)}
.risks-title{position:absolute;top:86px;left:0;width:1200px;text-align:center;font-size:34px;font-weight:500;line-height:46px}
.risk-card{position:absolute;width:211px;height:115px;background:#f6ead0;border-radius:6px;display:flex;align-items:flex-end;justify-content:center;padding-bottom:18px;text-align:center;font-size:15px;font-weight:500;line-height:20px;color:var(--ink)}
.risk-card.featured{background:var(--white);height:133px;padding-bottom:36px;box-shadow:0 10px 22px rgba(90,60,0,.18)}
.risk-icon{position:absolute;left:50%;top:-40px;margin-left:-40px;width:80px;height:80px;border-radius:50%;background:var(--brown);display:flex;align-items:center;justify-content:center}
.featured .risk-icon{background:var(--gold)}
.dot-line-v{position:absolute;width:0;border-left:2px dotted #555}

/* ciso */
.ciso{position:absolute;top:2205px;left:0;width:1200px;height:567px;background:var(--white)}
.ciso-title{position:absolute;left:115px;top:122px;font-size:26px;font-weight:500;line-height:37px}
.ciso-copy{position:absolute;left:115px;top:210px;width:470px;font-size:14.2px;line-height:23.6px}
.shield-ciso{left:682px;top:92px;width:370px;height:392px;background:linear-gradient(150deg,#0c2a55 0%,#1a5fa8 40%,#1a2437 70%,#6e5418 100%)}

/* testimonials */
.testimonials{position:absolute;top:2772px;left:0;width:1200px;height:436px;background:var(--slate)}
.t-title{position:absolute;top:76px;left:0;width:1200px;text-align:center;color:var(--white);font-size:25px;font-weight:500}
.avatar{position:absolute;left:277px;top:136px;width:124px;height:124px;border-radius:50%;background:radial-gradient(circle at 50% 40%,#d9c2b0 0%,#9a8272 55%,#ffffff 56%)}
.quote{position:absolute;left:457px;top:146px;width:500px;font-size:12.8px;line-height:22.6px;color:#eeeef2}
.qmark{position:absolute;font-family:Georgia,serif;font-size:40px;color:#e4e4ea;line-height:1}
.author{position:absolute;left:457px;top:245px;font-size:13.5px;font-weight:700;color:var(--white)}
.video-frame{position:absolute;left:299px;top:3118px;width:604px;height:398px;background:var(--white);border-radius:14px;box-shadow:0 12px 30px rgba(0,0,0,.15);padding:10px}
.video{width:100%;height:100%;border-radius:10px;background:linear-gradient(180deg,#2d5a80 0%,#1c3552 45%,#101c33 100%);position:relative}

/* news */
.news{position:absolute;top:3600px;left:0;width:1200px;height:528px;background:var(--paper)}
.news-title{position:absolute;top:68px;left:0;width:1200px;text-align:center;font-size:36px;font-weight:500}
.news-card{position:absolute;top:137px;width:270px}
.news-img{width:270px;height:181px}
.news-date{margin-top:16px;font-size:11px;color:var(--gold-deep)}
.news-head{margin-top:9px;font-size:13.5px;font-weight:700}
.news-text{margin-top:6px;font-size:11px;line-height:20px;color:var(--text)}
.news-more{margin-top:5px;font-size:10.5px;color:var(--gold-deep)}

/* footer */
.footer{position:absolute;top:4128px;left:0;width:1200px;height:350px;background:var(--white)}
.brand-foot{left:148px;top:52px;font-size:50px;color:var(--ink)}
.foot-about{position:absolute;left:148px;top:134px;width:230px;font-size:11.5px;line-height:20px;color:var(--text)}
.socials{position:absolute;left:148px;top:210px;display:flex;gap:5px}
.socials span{width:30px;height:30px;border-radius:50%;background:var(--gold)}
.foot-col{position:absolute;top:66px}
.foot-col h4{font-size:17px;font-weight:700;margin-bottom:12px}
.foot-col li{list-style:none;font-size:15px;line-height:24.5px;color:var(--muted)}
.foot-note{font-size:14.5px;line-height:22px;color:var(--muted);width:270px}
.signup{position:absolute;left:798px;top:181px;width:285px;height:42px;border:2px solid #b9b9c0;border-radius:21px;overflow:hidden;display:flex}
.signup .field{flex:1;padding-left:26px;font-size:13px;color:#9b9ba3;display:flex;align-items:center}
.signup .go{width:104px;background:var(--gold);font-size:14px;font-weight:500;display:flex;align-items:center;justify-content:center}
.foot-rule{position:absolute;left:95px;top:289px;width:1010px;border-top:1px solid #e3e3e8}
.copyright{position:absolute;left:0;top:310px;width:1200px;text-align:center;font-size:11.5px;color:var(--text)}
</style>
</head>
<body>

<!-- HERO -->
<div class="hero-bg"></div>
<svg class="hero-shape" width="1200" height="800" viewBox="0 0 1200 800">
  <defs>
    <linearGradient id="heroFill" x1="0" y1="0" x2="0.3" y2="1">
      <stop offset="0" stop-color="#151438"/>
      <stop offset="0.45" stop-color="#2a2466"/>
      <stop offset="0.8" stop-color="#5a2f98"/>
      <stop offset="1" stop-color="#8b3aa8"/>
    </linearGradient>
  </defs>
  <path role="img" aria-label="Security analysts at monitors over a glowing purple network mesh" d="M0 0H1200V470C1080 690 850 782 600 782C350 782 120 690 0 470Z" fill="url(#heroFill)"/>
  <path d="M0 474C120 698 350 790 600 790C850 790 1080 698 1200 474" fill="none" stroke="#f0c239" stroke-width="5"/>
</svg>

<div class="brand brand-hero">VELMORA</div>
<nav class="nav">
  <a class="active">Home</a><a>Q&amp;A</a><a>Pricing</a><a>About Us</a><a>Resources ▾</a>
</nav>
<a class="contact-btn">
  <svg width="14" height="14" viewBox="0 0 24 24"><path d="M6.6 10.8a15 15 0 0 0 6.6 6.6l2.2-2.2a1 1 0 0 1 1-.25 11.4 11.4 0 0 0 3.6.57 1 1 0 0 1 1 1V20a1 1 0 0 1-1 1A17 17 0 0 1 3 4a1 1 0 0 1 1-1h3.5a1 1 0 0 1 1 1c0 1.25.2 2.45.57 3.57a1 1 0 0 1-.25 1Z" fill="#3a3a42"/></svg>
  Contact Us
</a>

<h1 class="hero-title h1a">DEFEND AGAINST</h1>
<div class="hero-title h1b">CYBER-ATTACKS</div>
<div class="hero-title h1c">BEFORE THEY HAPPEN</div>
<p class="hero-lead">Velmora helps you understand when, where and how stolen or accidentally leaked information in dark web markets, forums, botnet logs, IRC, social media and other sources is exposed.</p>
<a class="demo-btn">LIVE DEMO TODAY!</a>

<div class="partners">
  <div class="partner" style="width:168px"></div>
  <div class="partner" style="width:112px"></div>
  <div class="partner" style="width:166px"></div>
  <div class="partner" style="width:174px"></div>
</div>

<!-- ABOUT -->
<section class="about">
  <div class="shield shield-about" role="img" aria-label="Hands typing on a laptop with a glowing padlock shield overlay"></div>
  <h2 class="section-title about-title">ABOUT VELM<span class="hl">ORA</span></h2>
  <div class="dot-end" style="left:1075px;top:105px"></div>
  <div class="dot-line-h" style="left:1082px;top:108px;width:118px"></div>
  <div class="about-copy body-copy">
    <p>Velmora helps you understand when, where and how stolen or accidentally leaked information&nbsp; in dark web markets, forums, botnet logs, IRC, social media and other sources is exposed.</p>
    <p>Velmora’s alerting service can also detect threats before they turn into incidents. Velmora offers AI-driven dark web analysis, real-time threat alerts and pre-Attack threat indicators. Setup in minutes you will receive instant access to real-time reporting including:</p>
  </div>
  <a class="outline-btn" style="left:602px;top:382px">LEARN MORE</a>
  <div class="dot-line-v" style="left:599px;top:508px;height:34px"></div>
</section>

<!-- RISKS -->
<section class="risks">
  <div class="dot-line-v" style="left:599px;top:0;height:46px"></div>
  <div class="dot-end" style="left:597px;top:44px;background:#555"></div>
  <h2 class="risks-title">WHAT RISKS CAN BE MITIGATED<br>WITH VELMORA?</h2>

  <div class="risk-card" style="left:148px;top:244px">
    <span class="risk-icon"><svg width="40" height="40" viewBox="0 0 40 40"><rect x="6" y="12" width="28" height="18" rx="3" fill="none" stroke="#f0c239" stroke-width="3"/><circle cx="14" cy="21" r="2" fill="#f0c239"/><circle cx="20" cy="21" r="2" fill="#f0c239"/><circle cx="26" cy="21" r="2" fill="#f0c239"/></svg></span>
    Prevent Phishing
  </div>
  <div class="risk-card featured" style="left:379px;top:244px">
    <span class="risk-icon"><svg width="40" height="40" viewBox="0 0 40 40"><circle cx="20" cy="20" r="7" fill="none" stroke="#5a4010" stroke-width="3"/><path d="M20 4v8M20 28v8M4 20h8M28 20h8M9 9l5 5M26 26l5 5M31 9l-5 5M9 31l5-5" stroke="#5a4010" stroke-width="3"/></svg></span>
    Detect Exposed<br>Infrastructure
  </div>
  <div class="risk-card" style="left:610px;top:244px">
    <span class="risk-icon"><svg width="40" height="40" viewBox="0 0 40 40"><rect x="7" y="8" width="26" height="18" rx="2" fill="none" stroke="#f0c239" stroke-width="3"/><path d="M14 32h12M20 26v6" stroke="#f0c239" stroke-width="3"/></svg></span>
    Detect Leaks from<br>Ransomware
  </div>
  <div class="risk-card" style="left:842px;top:244px">
    <span class="risk-icon"><svg width="40" height="40" viewBox="0 0 40 40"><circle cx="20" cy="20" r="5" fill="#f0c239"/><circle cx="8" cy="9" r="3" fill="#f0c239"/><circle cx="32" cy="9" r="3" fill="#f0c239"/><circle cx="8" cy="31" r="3" fill="#f0c239"/><circle cx="32" cy="31" r="3" fill="#f0c239"/><path d="M10 11l7 7M30 11l-7 7M10 29l7-7M30 29l-7-7" stroke="#f0c239" stroke-width="2.5"/></svg></span>
    Find Exposed Data<br>in the Darknet
  </div>

  <div class="risk-card" style="left:148px;top:442px">
    <span class="risk-icon"><svg width="40" height="40" viewBox="0 0 40 40"><path d="M8 16h10l12-7v22l-12-7H8z" fill="none" stroke="#f0c239" stroke-width="3" stroke-linejoin="round"/></svg></span>
    Detect spoofing and<br>Impersonation
  </div>
  <div class="risk-card" style="left:379px;top:442px">
    <span class="risk-icon"><svg width="40" height="40" viewBox="0 0 40 40"><circle cx="20" cy="13" r="5" fill="#f0c239"/><path d="M11 32a9 9 0 0 1 18 0z" fill="#f0c239"/><circle cx="8" cy="18" r="3" fill="#f0c239"/><circle cx="32" cy="18" r="3" fill="#f0c239"/></svg></span>
    Understand Employee<br>Exposure
  </div>
  <div class="risk-card" style="left:610px;top:442px">
    <span class="risk-icon"><svg width="40" height="40" viewBox="0 0 40 40"><circle cx="17" cy="17" r="10" fill="none" stroke="#f0c239" stroke-width="3"/><path d="M24 24l9 9" stroke="#f0c239" stroke-width="4" stroke-linecap="round"/><path d="M12 17l4 4 6-7" fill="none" stroke="#f0c239" stroke-width="3"/></svg></span>
    Detect Stolen Data
  </div>
  <div class="risk-card" style="left:842px;top:442px">
    <span class="risk-icon"><svg width="40" height="40" viewBox="0 0 40 40"><path d="M20 5l15 27H5z" fill="none" stroke="#f0c239" stroke-width="3" stroke-linejoin="round"/><path d="M20 15v8" stroke="#f0c239" stroke-width="3"/><circle cx="20" cy="27" r="1.8" fill="#f0c239"/></svg></span>
    And Many More<br>Risk Indicators
  </div>
</section>

<!-- CISO -->
<section class="ciso">
  <div class="dot-line-h" style="left:0;top:139px;width:78px"></div>
  <div class="dot-end" style="left:77px;top:136px"></div>
  <h2 class="ciso-title">THE CISO’S SOLUTION – FOREWARNED<br>IS FOREARMED</h2>
  <p class="ciso-copy body-copy">Velmora helps you understand when, where and how stolen or accidentally leaked information is exposed. Velmora’s alerting service can also detect threats before they turn into incidents. There are certain indicators that can be measured. Before an attack takes place, hackers often reserve similar domain names (typosquatting), they spoof profiles in social media like Linkora or they exchange information about targets in hacker forums.</p>
  <a class="outline-btn" style="left:117px;top:398px">LEARN MORE</a>
  <div class="shield shield-ciso" role="img" aria-label="Hooded figure raising a glowing digital hand beside a laptop"></div>
</section>

<!-- TESTIMONIALS -->
<section class="testimonials">
  <h2 class="t-title">TESTIMONIALS</h2>
  <svg class="abs" style="left:200px;top:172px" width="24" height="40" viewBox="0 0 24 40"><path d="M20 4L4 20l16 16" fill="none" stroke="#fff" stroke-width="2.5"/></svg>
  <svg class="abs" style="left:976px;top:172px" width="24" height="40" viewBox="0 0 24 40"><path d="M4 4l16 16L4 36" fill="none" stroke="#fff" stroke-width="2.5"/></svg>
  <div class="avatar" role="img" aria-label="Portrait of the quoted client"></div>
  <span class="qmark" style="left:424px;top:140px">“</span>
  <p class="quote">Lorem Ipsum is simply dummy text of the printing and typesetting industry. Lorem Ipsum has been the industry's standard dummy text ever since the 1500s, when an unknown printer took a galley of type and scrambled it to make a type specimen book.</p>
  <span class="qmark" style="left:630px;top:226px">”</span>
  <div class="author">By Author Name</div>
</section>

<div class="video-frame">
  <div class="video" role="img" aria-label="Night city skyline with glowing blue data network lines">
    <svg class="abs" style="left:256px;top:160px" width="72" height="72" viewBox="0 0 72 72"><circle cx="36" cy="36" r="35" fill="#fff"/><path d="M29 23l21 13-21 13z" fill="#1b1b1f"/></svg>
  </div>
</div>

<!-- NEWS -->
<section class="news">
  <h2 class="section-title news-title">LATEST <span class="hl">NEWS</span></h2>
  <article class="news-card" style="left:157px">
    <div class="news-img" role="img" aria-label="Hands cupping a glowing padlock shield" style="background:linear-gradient(160deg,#2a0f16,#3a1f3f 50%,#1b3a7a)"></div>
    <div class="news-date">January 30, 2022</div>
    <div class="news-head">Lorem Ipsum is simply dummy</div>
    <p class="news-text">Lorem Ipsum has been the industry's standard dummy text ever since the 1500s,</p>
    <div class="news-more">CONTINUE READING ⊙</div>
  </article>
  <article class="news-card" style="left:464px">
    <div class="news-img" role="img" aria-label="Glowing blue padlock in a circuit ring" style="background:radial-gradient(circle at 40% 50%,#4fa6e8,#14407e 45%,#0a1c3e)"></div>
    <div class="news-date">January 30, 2022</div>
    <div class="news-head">Lorem Ipsum is simply dummy</div>
    <p class="news-text">Lorem Ipsum has been the industry's standard dummy text ever since the 1500s,</p>
    <div class="news-more">CONTINUE READING ⊙</div>
  </article>
  <article class="news-card" style="left:774px">
    <div class="news-img" role="img" aria-label="Hooded hacker in front of code screens" style="background:linear-gradient(120deg,#0b1f4a,#1a4aa0 55%,#0e2150)"></div>
    <div class="news-date">January 30, 2022</div>
    <div class="news-head">Lorem Ipsum is simply dummy</div>
    <p class="news-text">Lorem Ipsum has been the industry's standard dummy text ever since the 1500s,</p>
    <div class="news-more">CONTINUE READING ⊙</div>
  </article>
</section>

<!-- FOOTER -->
<footer class="footer">
  <div class="brand brand-foot">VELMORA</div>
  <p class="foot-about">Lorem Ipsum has been the industry's standard dummy text ever since the 1500s,</p>
  <div class="socials"><span></span><span></span><span></span><span></span></div>

  <div class="foot-col" style="left:431px">
    <h4>INFO</h4>
    <ul><li>Home</li><li>Q&amp;A</li><li>Pricing</li><li>About Us</li><li>Contact</li></ul>
  </div>
  <div class="foot-col" style="left:598px">
    <h4>RESOURCES</h4>
    <ul><li>Screenshots</li><li>News</li><li>Partner Program</li><li>Wiki</li><li>References</li><li>In the Press</li></ul>
  </div>
  <div class="foot-col" style="left:795px">
    <h4>SIGN UP FOR NEWSLETTER</h4>
    <p class="foot-note">If you&nbsp; have any questions please send us a message.</p>
  </div>
  <div class="signup"><span class="field">Email address</span><span class="go">Subscribe</span></div>

  <div class="foot-rule"></div>
  <div class="copyright">© 2022 velmora. All Rights are Reserved.</div>
</footer>

</body>
</html>
```